Business Card Design Project

We need a business card for our IT services provider business. We provide services to small and medium business, and would like something that reflects the color scheme / branding on our recently updated website - www.tallobrix.com.au

The card type we have chosen is a matte laminated double sided configuration at 86mm x 54mm on 350 GSM cardboard.
Updates

Target Market(s)

Small and Medium Business owners

Industry/Entity Type

Business

Requirements
Must have
• *Details on all cards*

Company Name: Tallobrix Pty Ltd
ABN: 52 683 914 207
Address: 47-49 Pembury Street, Ashcombe Vale, Victoria 3172
Phone: 1300 GRAB UP
Fax: 03 9417 6258
Website: www.tallobrix.com.au
Logo/Handprint Icon

*Person Specific*

```html
<!DOCTYPE html>
<html lang="en">
<head>
<meta charset="utf-8">
<title>Tallobrix Business Card</title>
<link rel="stylesheet" href="https://fonts.googleapis.com/css2?family=Tinos:wght@400;700&display=swap">
<style>
  :root {
    --brand-blue: #1e62a6;
    --brand-blue-dark: #174f87;
    --ink: #161616;
    --paper: #ffffff;
    --stage: #e4e4e4;
    --muted: #d4d4d4;
    --navy-text: #1d2e44;
  }
  * { box-sizing: border-box; margin: 0; padding: 0; }
  html, body {
    width: 1200px; height: 900px; overflow: hidden;
    background: var(--stage);
    font-family: "Tinos", "Times New Roman", serif;
  }
  .sheet {
    width: 1200px; height: 900px;
    display: flex; flex-direction: column; align-items: center; justify-content: center;
    gap: 28px;
  }
  .card {
    width: 640px; height: 402px; position: relative; overflow: hidden;
    box-shadow: 0 6px 18px rgba(0,0,0,0.18);
  }

  /* Back side */
  .card-back { background: var(--brand-blue); color: var(--paper); }
  .card-back .wordmark {
    position: absolute; left: 0; right: 0; top: 150px; text-align: center;
    font-size: 64px; font-weight: 400; letter-spacing: 1px; color: var(--paper);
  }
  .card-back .website {
    position: absolute; right: 44px; bottom: 34px;
    font-size: 17px; color: var(--paper);
  }

  /* Front side */
  .card-front { background: var(--paper); }
  .front-top {
    position: absolute; left: 0; top: 0; width: 100%; height: 218px;
    background: var(--brand-blue);
  }
  .contact-list {
    position: absolute; left: 34px; top: 26px; list-style: none;
    color: var(--paper); font-size: 15px; line-height: 26px;
  }
  .contact-list li { display: flex; align-items: center; gap: 8px; }
  .contact-list svg { width: 15px; height: 15px; flex: none; fill: var(--paper); }
  .contact-list .abn-label { font-size: 12px; width: 15px; letter-spacing: -0.5px; }
  .front-rule {
    position: absolute; left: 0; top: 218px; width: 100%; height: 3px; background: var(--paper);
  }
  .front-band {
    position: absolute; left: 0; top: 221px; width: 100%; height: 36px;
    background: var(--ink);
    display: flex; align-items: center; justify-content: space-between;
    padding: 0 30px;
  }
  .person-name { color: var(--paper); font-size: 22px; font-weight: 700; }
  .person-title { color: var(--muted); font-size: 16px; }
  .front-wordmark {
    position: absolute; left: 0; right: 0; top: 300px; text-align: center;
    font-size: 46px; color: var(--navy-text); letter-spacing: 1px;
  }
</style>
</head>
<body>
<main class="sheet">
  <section class="card card-back" aria-label="Card back">
    <div class="wordmark">Tallobrix</div>
    <div class="website">www.tallobrix.com.au</div>
  </section>

  <section class="card card-front" aria-label="Card front">
    <div class="front-top">
      <ul class="contact-list">
        <li><svg viewBox="0 0 16 16" aria-hidden="true"><path d="M8 1 1 7.5h2V15h4v-4h2v4h4V7.5h2z"/></svg>47-49 Pembury Street, Ashcombe Vale, Victoria 3172</li>
        <li><svg viewBox="0 0 16 16" aria-hidden="true"><path d="M1 3h14v10H1z M1 3l7 6 7-6" stroke="#1e62a6" stroke-width="1.2"/></svg>firstnamelastname@postwell.in</li>
        <li><svg viewBox="0 0 16 16" aria-hidden="true"><circle cx="8" cy="8" r="7"/><path d="M1 8h14M8 1c-3 3-3 11 0 14M8 1c3 3 3 11 0 14" stroke="#1e62a6" stroke-width="1" fill="none"/></svg>www.tallobrix.com.au</li>
        <li><svg viewBox="0 0 16 16" aria-hidden="true"><path d="M4 1 6.5 4 5 6c1 2 3 4 5 5l2-1.5 3 2.5-2 3C7 14 2 9 1 3z"/></svg>1300 GRAB UP</li>
        <li><svg viewBox="0 0 16 16" aria-hidden="true"><path d="M4 1 6.5 4 5 6c1 2 3 4 5 5l2-1.5 3 2.5-2 3C7 14 2 9 1 3z"/></svg>03 9417 6258</li>
        <li><svg viewBox="0 0 16 16" aria-hidden="true"><path d="M2 5h12v9H2z M4 1h7v4H4z"/><rect x="4" y="8" width="8" height="1.5" fill="#1e62a6"/></svg>932 781 4056</li>
        <li><span class="abn-label">ABN</span>52 683 914 207</li>
      </ul>
    </div>
    <div class="front-rule"></div>
    <div class="front-band">
      <span class="person-name">FirstName LastName</span>
      <span class="person-title">Founder and Managing Director</span>
    </div>
    <div class="front-wordmark">Tallobrix</div>
  </section>
</main>
</body>
</html>
```